Webdesign for large cottage directory

We have developed a first version of a website that can accommodate large groups (10 to 300 people). The site is English and is aimed at a wide audience ranging from a group of students to a family or a family. For the visitors the site is free and it is the propietaires who pay to see their accommodation. The site is online with just a few fake lodgings and a simple design to the elements that must be appraised (nothing to keep the current design). Our website is here: lodgevista.com (login / pass = admin / 123) Home page (lodgevista.com): on this page section) and lodging by theme (third section). These three points should be highlighted as possible. The displayed map may be slightly modified. Only the background and the color changes when hovering over the mouse. It can be enlarged / retreciated. Below these 3 sections we have some fairly published articles, the latest blog posts and the footer. The menu will be visible throughout the site. Category page (https://lodgevista.fr/gite-departement/aveyron OR https://lodgevista.fr/gites-couchages-121): On these pages we always return the same format with the googlemap, an image 1 text. Below the list of the cottages concerned and the filter options. Product page: The pages presenting the cottages can be of two types: - Either the cottage has no owner and there is no contact for the visitor to the owner that he can retrieve his cottage by registering: example of a page of this type: https://lodgevista.fr/domaine-de-fressanac - The cottage to a propietaire and we are on the classic card. : // lodgevista. en / domain-of-fressanac2 For all products on the site we have nav tab. It's just for testing. We do not want to be in the design for real website. All information must be in the page without login / register page: classic, it's here: https://lodgevista.it/login and https://lodgevista.fr/register Blog homepage (https://lodgevista.fr/blog ): Classic blog page Blog post (https://lodgevista.fr/blog/urltemporaire1551521154) and static page (https://lodgevista.fr/blog/Systeme-classement-lodgevistafr): Nothing special Menu: Menu is an important part of the website. It's the way to navigate on the wbesite.
Faible participation designers
Number of Pages Required
4 page
Colors
Designer to choose colors to be used in the design.
Look and feel
Each slider illustrates characteristics of the customer's brand and the style your logo design should communicate.

```html
<!DOCTYPE html>
<html lang="fr">
<head>
<meta charset="utf-8">
<title>lodgevista.fr – Accueil</title>
<link href="https://fonts.googleapis.com/css2?family=Nunito+Sans:wght@400;600;700;800&display=swap" rel="stylesheet">
<style>
:root{
  --blue:#3d5bd9;
  --ink:#1a1a1a;
  --muted:#444;
  --grey-band:#ebebeb;
  --white:#fff;
  --stage:#f7f7f7;
}
*{box-sizing:border-box;margin:0;padding:0}
html,body{width:1200px;height:1200px;overflow:hidden;background:var(--stage);font-family:"Nunito Sans",Arial,sans-serif;color:var(--ink)}
.page{position:absolute;left:359px;top:8px;width:482px;height:1192px;background:var(--white);box-shadow:0 0 40px rgba(0,0,0,.18);overflow:hidden}
.inner{position:absolute;left:35px;width:413px}

/* hero */
.hero{position:absolute;left:0;top:0;width:482px;height:270px;
  background:
    radial-gradient(ellipse 140px 60px at 300px 215px,rgba(120,70,40,.75),rgba(120,70,40,0)),
    radial-gradient(ellipse 200px 120px at 420px 150px,rgba(20,55,35,.9),rgba(20,55,35,0)),
    radial-gradient(ellipse 160px 90px at 230px 70px,rgba(150,145,140,.8),rgba(150,145,140,0)),
    linear-gradient(180deg,#3b4654 0%,#6f767d 20%,#5a6060 36%,#2f4a3b 50%,#1e6f6a 62%,#2f8a83 74%,#1f4f4a 88%,#22302e 100%)}
.topnav{position:absolute;left:35px;top:9px;width:413px;height:14px;display:flex;align-items:center}
.brand{font-weight:800;font-size:10px;color:var(--white);letter-spacing:-.2px}
.menu{display:flex;gap:10px;margin-left:auto;margin-right:12px}
.menu a{color:var(--white);font-size:4.4px;font-weight:700;text-decoration:none}
.login{background:var(--blue);color:var(--white);font-size:4.4px;font-weight:700;padding:2px 4px;border-radius:1px}
.hero-copy{position:absolute;left:35px;top:94px;width:175px;color:var(--white)}
.hero-copy h1{font-size:14px;font-weight:700;line-height:18px;text-shadow:0 1px 3px rgba(0,0,0,.4)}
.hero-copy p{font-size:5px;font-weight:700;line-height:7px;margin-top:5px;text-shadow:0 1px 2px rgba(0,0,0,.5)}
.cta{display:inline-block;margin-top:5px;background:var(--blue);color:var(--white);font-size:4.2px;font-weight:700;padding:2.5px 6px;border-radius:1px}

/* tabs */
.tabs{position:absolute;left:0;top:270px;width:482px;height:20px;background:var(--blue)}
.tabs ul{list-style:none;display:flex;gap:12px;position:absolute;left:35px;top:4px}
.tabs li{color:var(--white);font-size:8px;font-weight:700;line-height:11px}
.tabs li.active{border-bottom:1px solid #cbd6ff}

/* themes */
.themes{top:302px;display:grid;grid-template-columns:repeat(4,100px);gap:8px 4px}
.theme{position:relative;height:65px;box-shadow:0 1px 2px rgba(0,0,0,.25)}
.theme .label{position:absolute;left:0;bottom:0;width:80%;height:8px;background:var(--blue);color:var(--white);font-size:5.5px;font-weight:700;padding:1px 0 0 7px}
.theme .underline{position:absolute;left:0;bottom:0;width:100%;height:1.5px;background:var(--blue)}
.ph-seminar{background:
  linear-gradient(180deg,#e6e9ec 0%,#c4ccd3 30%,#a9b3bb 50%,#8a6242 68%,#c47a45 82%,#3d3430 100%)}
.ph-fishing{background:linear-gradient(180deg,#2e4470 0%,#7a6a7a 25%,#f09a35 45%,#f8c060 52%,#d8843a 62%,#34405a 80%,#5a4a3c 100%)}
.ph-water{background:radial-gradient(ellipse 60px 30px at 40% 25%,#5fb6ea,rgba(95,182,234,0)),linear-gradient(180deg,#2a86cc 0%,#1d68b0 50%,#0e3c76 100%)}
.ph-riding{background:radial-gradient(ellipse 30px 20px at 50% 55%,#8a4a28,rgba(138,74,40,0)),linear-gradient(180deg,#5e7a4a 0%,#7d8a6a 35%,#8e6a4a 55%,#b0a890 80%,#d6d4cc 100%)}

/* latest */
.latest{position:absolute;left:0;top:458px;width:482px;height:436px;background:var(--grey-band)}
.section-title{font-size:8px;font-weight:700;color:var(--blue)}
.latest .section-title{position:absolute;left:35px;top:12px}
.ph-cottage{background:
  radial-gradient(ellipse 45px 30px at 40% 62%,#b89064,rgba(184,144,100,0)),
  linear-gradient(180deg,#0c2570 0%,#163a94 40%,#5a6a8a 56%,#a08a68 66%,#7a808c 80%,#e0dcd4 100%)}
.card{position:absolute;background:var(--white);box-shadow:0 1px 3px rgba(0,0,0,.25);display:flex}
.card .photo{flex:none}
.card .info{position:relative;font-size:3.6px;line-height:4.8px;color:var(--muted)}
.card .info b{color:var(--ink)}
.card .name{font-size:4.6px;font-weight:700;color:var(--ink);margin-bottom:2px}
.card .row{margin-bottom:2px}
.book{position:absolute;background:var(--blue);color:var(--white);font-size:4.2px;font-weight:700;text-align:center;height:8px;line-height:8px;border-radius:1px;box-shadow:0 1px 1.5px rgba(0,0,0,.3)}
.card-small{width:205px;height:117px;top:33px}
.card-small .photo{width:100px;height:117px}
.card-small .info{width:105px;padding:4px 4px 0}
.card-small .book{left:104px;right:4px;bottom:4px}
.card-wide{left:35px;width:413px;height:87px}
.card-wide .photo{width:134px;height:87px}
.card-wide .info{display:flex;gap:8px;width:279px;padding:5px 6px 0 4px}
.card-wide .col-a{width:96px}
.card-wide .col-b{width:163px}
.card-wide .book{right:8px;bottom:5px;width:55px}

/* blog */
.blog-title{position:absolute;left:35px;top:901px;text-decoration:underline}
.blog{top:914px;display:grid;grid-template-columns:repeat(3,134px);gap:5px}
.post .photo{height:115px}
.post h3{font-size:5px;font-weight:700;margin-top:7px}
.post p{font-size:3.6px;line-height:4.6px;color:var(--muted);margin-top:4px}

/* footer */
.footer{position:absolute;left:0;top:1094px;width:482px;height:86px;background:var(--blue);color:var(--white);font-size:7px;font-weight:800;display:flex;align-items:center;justify-content:center;letter-spacing:.2px}
</style>
</head>
<body>
<div class="page">

  <header class="hero" role="img" aria-label="Photo: wooden boathouse on a turquoise mountain lake under rocky peaks and pine forest">
    <nav class="topnav">
      <span class="brand">lodgevista.fr</span>
      <div class="menu">
        <a>Gite par capacité</a><a>Gite par département</a><a>Gite par thématique</a><a>Blog</a><a>Vos favoris</a>
      </div>
      <span class="login">Connexion</span>
    </nav>
    <div class="hero-copy">
      <h1>Réservez votre chalet de rêve aujourd'hui!</h1>
      <p>Choisissez parmi différentes destinations magnifiques autour de la France. Du plus petit au plus grand, nous vous aiderons à trouver et à réserver le chalet que vous recherchez.</p>
      <span class="cta">Trouve maintenant</span>
    </div>
  </header>

  <nav class="tabs">
    <ul><li>Gites par capacités</li><li>Gites par departement</li><li class="active">Gites par thématique</li></ul>
  </nav>

  <section class="inner themes">
    <div class="theme ph-seminar" role="img" aria-label="Photo: group meeting around a conference table"><span class="underline"></span><span class="label">Séminaire</span></div>
    <div class="theme ph-fishing" role="img" aria-label="Photo: angler on a pier at sunset"><span class="underline"></span><span class="label">Pêche</span></div>
    <div class="theme ph-water" role="img" aria-label="Photo: manta ray swimming in blue water"><span class="underline"></span><span class="label">Aquatique</span></div>
    <div class="theme ph-riding" role="img" aria-label="Photo: rider jumping a horse over a fence"><span class="underline"></span><span class="label">Equitation</span></div>
    <div class="theme ph-seminar" role="img" aria-label="Photo: group meeting around a conference table"><span class="underline"></span><span class="label">Séminaire</span></div>
    <div class="theme ph-fishing" role="img" aria-label="Photo: angler on a pier at sunset"><span class="underline"></span><span class="label">Pêche</span></div>
    <div class="theme ph-water" role="img" aria-label="Photo: manta ray swimming in blue water"><span class="underline"></span><span class="label">Aquatique</span></div>
    <div class="theme ph-riding" role="img" aria-label="Photo: rider jumping a horse over a fence"><span class="underline"></span><span class="label">Equitation</span></div>
  </section>

  <section class="latest">
    <h2 class="section-title">Last 5 lodgings added</h2>

    <article class="card card-small" style="left:35px">
      <div class="photo ph-cottage" role="img" aria-label="Photo: row of wooden cottages under a deep blue sky"></div>
      <div class="info">
        <div class="name">Cottage name</div>
        <div class="row"><b>Adresse:</b> 14 Chemin des Pins, Annecy 74000, France</div>
        <div class="row"><b>Region:</b> Guadeloupe</div>
        <div class="row"><b>Departement:</b> Guadeloupe</div>
        <div class="row"><b>Capacite:</b> 13</div>
        <div class="row"><b>Formule proposée:</b> Gîte entier</div>
        <div class="row"><b>Description :</b> Spacious stone lodge near the lake with a shared kitchen, large dining hall, quiet gardens and plenty of beds for big groups and families.</div>
      </div>
      <span class="book">Réserve</span>
    </article>

    <article class="card card-small" style="left:243px">
      <div class="photo ph-cottage" role="img" aria-label="Photo: row of wooden cottages under a deep blue sky"></div>
      <div class="info">
        <div class="name">Cottage name</div>
        <div class="row"><b>Adresse:</b> 14 Chemin des Pins, Annecy 74000, France</div>
        <div class="row"><b>Region:</b> Guadeloupe</div>
        <div class="row"><b>Departement:</b> Guadeloupe</div>
        <div class="row"><b>Capacite:</b> 13</div>
        <div class="row"><b>Formule proposée:</b> Gîte entier</div>
        <div class="row"><b>Description :</b> Spacious stone lodge near the lake with a shared kitchen, large dining hall, quiet gardens and plenty of beds for big groups and families.</div>
      </div>
      <span class="book">Réserve</span>
    </article>

    <article class="card card-wide" style="top:155px">
      <div class="photo ph-cottage" role="img" aria-label="Photo: row of wooden cottages under a deep blue sky"></div>
      <div class="info">
        <div class="col-a">
          <div class="name">Cottage name</div>
          <div><b>Adresse:</b> 14 Chemin des Pins, Annecy 74000, France</div>
          <div><b>Region:</b> Guadeloupe</div>
          <div><b>Departement:</b> Guadeloupe</div>
          <div><b>Capacite:</b> 13</div>
          <div><b>Formule proposée:</b> Gîte entier</div>
        </div>
        <div class="col-b" style="margin-top:6.6px"><b>Description :</b> Spacious stone lodge near the lake with a shared kitchen, large dining hall, quiet gardens and plenty of beds for big groups.</div>
      </div>
      <span class="book">Réserve</span>
    </article>

    <article class="card card-wide" style="top:248px">
      <div class="photo ph-cottage" role="img" aria-label="Photo: row of wooden cottages under a deep blue sky"></div>
      <div class="info">
        <div class="col-a">
          <div class="name">Cottage name</div>
          <div><b>Adresse:</b> 14 Chemin des Pins, Annecy 74000, France</div>
          <div><b>Region:</b> Guadeloupe</div>
          <div><b>Departement:</b> Guadeloupe</div>
          <div><b>Capacite:</b> 13</div>
          <div><b>Formule proposée:</b> Gîte entier</div>
        </div>
        <div class="col-b" style="margin-top:6.6px"><b>Description :</b> Spacious stone lodge near the lake with a shared kitchen, large dining hall, quiet gardens and plenty of beds for big groups.</div>
      </div>
      <span class="book">Réserve</span>
    </article>

    <article class="card card-wide" style="top:340px">
      <div class="photo ph-cottage" role="img" aria-label="Photo: row of wooden cottages under a deep blue sky"></div>
      <div class="info">
        <div class="col-a">
          <div class="name">Cottage name</div>
          <div><b>Adresse:</b> 14 Chemin des Pins, Annecy 74000, France</div>
          <div><b>Region:</b> Guadeloupe</div>
          <div><b>Departement:</b> Guadeloupe</div>
          <div><b>Capacite:</b> 13</div>
          <div><b>Formule proposée:</b> Gîte entier</div>
        </div>
        <div class="col-b" style="margin-top:6.6px"><b>Description :</b> Spacious stone lodge near the lake with a shared kitchen, large dining hall, quiet gardens and plenty of beds for big groups.</div>
      </div>
      <span class="book">Réserve</span>
    </article>
  </section>

  <h2 class="section-title blog-title">Blog</h2>
  <section class="inner blog">
    <article class="post">
      <div class="photo ph-seminar" role="img" aria-label="Photo: team meeting in a bright office"></div>
      <h3>Post title 1</h3>
      <p>Short notes on planning a group stay, choosing the right lodge and sharing tasks with everyone.</p>
    </article>
    <article class="post">
      <div class="photo ph-seminar" role="img" aria-label="Photo: team meeting in a bright office"></div>
      <h3>Post title 1</h3>
      <p>Short notes on planning a group stay, choosing the right lodge and sharing tasks with everyone.</p>
    </article>
    <article class="post">
      <div class="photo ph-seminar" role="img" aria-label="Photo: team meeting in a bright office"></div>
      <h3>Post title 1</h3>
      <p>Short notes on planning a group stay, choosing the right lodge and sharing tasks with everyone.</p>
    </article>
  </section>

  <footer class="footer">FOOTER CONTENT</footer>
</div>
</body>
</html>
```